Harbor Crest Physician Advising

I need a one-page advertisement that I can email to potential clients.

The target audience is hospital administrators.

I want it to include the logo, as attached. We specialize in Payer Denial Management. We are certified physician advisors with over 80 years combined clinical medicine experience. We have expertise in Utilization Management, Clinical Documentation Integrity, Peer to Peer Appeals and Letter Appeal Management. We win over 60% of our Peer to Peer Appeals with Medicare Advantage plans and over 50% of our first level letters.

We make sure hospitals get paid for the care they provide, I really want to emphasize that we are very effective at overturning insurance payment denials. We also provider other physician advising services. We keep our company small so that our rates are very affordable. Include that references are available.

We need to include: Contact us today, we can improve your revenue. Please 304-555-0183
or email (I will provide this later).

I want it to look professional but not bland, with maybe AI created images of a small group of physicians (mature, white coats, stethoscopes) looking at a spreadsheet on a laptop. a picture of a stack of money setting on a table, with a hand removing part of the money from the stack.

Companies like ours include Quorvix, T7, Pellingham, Car-Nova, and TelvanMD. Their websites may provide ideas.

Target Market(s)

Healthcare administrators who need to improve their hospital revenue

Industry/Entity Type

Healthcare consulting

Font styles to use
Sans Serif

Colors
0094D4
00A9DD
6FCCEA
C7EBF8
E9F6FB
00AB8E
00BBA5
67D7C9
C6EFE9
E9F9F6
FFC000
F8CF3A
FAE287
FDF2CF
FEFAEE
EE7325
F08F49
F5BC92
FAE3D3
FDF4ED
E54698
E96AAD
F1A4CE
F9D9EA
FCEFF6
6B429C
8869AF
B7A5CE
E3DAEB
F3F0F8

Requirements
Must have
• Must include that we are very successful here to appear in Peer to Peer appeals and Letter appeals
Nice to have
• Very easy to read, big bold fonts
Should not have
• I’m very afraid of having a lot of dark blues, combined with dark gold, because it may look like the colors of a health system in my area

```html
<!DOCTYPE html>
<html lang="en">
<head>
<meta charset="UTF-8">
<title>Harbor Crest Physician Advising</title>
<link rel="stylesheet" href="https://fonts.googleapis.com/css2?family=Poppins:wght@400;500;600;700;800&display=swap">
<style>
  :root {
    --sky-photo-start: #8eaecd;
    --sky-photo-end: #dfe7ef;
    --gold: #fbbd0c;
    --cream: #fdfbf0;
    --white: #ffffff;
    --ink: #1b1b1b;
    --teal: #12a98c;
    --blue-title: #1e8fd6;
    --orange: #ee7325;
    --highlight: #fae287;
    --money-warm: #e3dccb;
    --money-green: #b8c4ad;
  }
  * { margin: 0; padding: 0; box-sizing: border-box; }
  html, body { width: 848px; height: 1200px; overflow: hidden; background: var(--white); }
  body { font-family: "Poppins", sans-serif; color: var(--ink); }
  .poster { position: relative; width: 848px; height: 1200px; overflow: hidden;
    background: linear-gradient(160deg, #ffffff 0%, #f4f6f8 55%, #ffffff 100%); }

  .hero-photo { position: absolute; left: 0; top: 0; width: 848px; height: 628px;
    background: linear-gradient(100deg, var(--sky-photo-start) 0%, #b3c8dd 45%, var(--sky-photo-end) 100%); }

  .brand { position: absolute; left: 40px; top: 45px; width: 300px; display: flex; flex-direction: column; align-items: center; color: var(--white); font-weight: 700; }
  .brand-mark { width: 64px; height: 64px; border-radius: 50%; background: var(--white); opacity: 0.9; margin-bottom: 22px; }
  .brand-name { font-size: 37px; line-height: 1; letter-spacing: -0.5px; white-space: nowrap; }
  .brand-tagline { font-size: 19px; line-height: 1; margin-top: 3px; letter-spacing: 0.3px; white-space: nowrap; }

  .hero-panel { position: absolute; left: 0; top: 0; width: 848px; height: 628px; }

  .headline-text { position: absolute; left: 26px; font-weight: 700; line-height: 1; white-space: nowrap; letter-spacing: 1px; }
  .headline-accent { top: 324px; color: var(--gold); font-size: 84px; }
  .headline-care { top: 399px; color: var(--cream); font-size: 54px; }
  .headline-provide { top: 449px; color: var(--cream); font-size: 54px; }
  .headline-rule { position: absolute; left: 26px; top: 503px; width: 368px; height: 8px; background: var(--gold); }
  .subhead { position: absolute; left: 27px; top: 519px; color: var(--white); font-size: 28px; line-height: 36px; font-weight: 400; letter-spacing: 0.3px; white-space: nowrap; }

  .money-photo { position: absolute; left: 491px; top: 658px; width: 350px; height: 345px;
    background: radial-gradient(ellipse at 55% 45%, var(--money-green) 0%, var(--money-warm) 45%, rgba(255,255,255,0) 72%); }

  .section-title { position: absolute; font-weight: 800; font-size: 33px; line-height: 1; letter-spacing: -1.2px; display: flex; align-items: center; white-space: nowrap; }
  .section-title svg { flex: none; }
  .title-stats { left: 27px; top: 682px; color: var(--teal); }
  .title-stats svg { margin-right: 19px; }
  .title-services { left: 27px; top: 806px; color: var(--blue-title); }
  .title-services svg { margin-right: 17px; }
  .title-strength { left: 27px; top: 1035px; color: var(--orange); }
  .title-strength svg { margin-right: 24px; }

  .list { position: absolute; list-style: none; font-size: 16px; }
  .list li { display: flex; align-items: center; height: 27px; white-space: nowrap; }
  .list svg { flex: none; margin-right: 11px; }

  .stats-list { left: 25px; top: 725px; }
  .stats-list li { background: var(--highlight); padding: 0 4px 0 2px; height: 24px; margin-bottom: 5px; width: max-content; }
  .services-list { left: 27px; top: 845px; }
  .strength-list { left: 27px; top: 1083px; }
  .strength-list svg { margin-right: 15px; }

  .contact-panel { position: absolute; left: 0; top: 0; width: 848px; height: 1200px; pointer-events: none; }
  .contact { position: absolute; right: 23px; top: 1058px; width: 380px; text-align: right; color: var(--white); }
  .contact-title { font-size: 32px; font-weight: 700; letter-spacing: 1.5px; line-height: 1; white-space: nowrap; }
  .contact-rule { height: 2px; width: 328px; background: var(--white); margin: 8px 0 0 auto; }
  .contact-line { font-size: 16.5px; letter-spacing: 1.6px; margin-top: 9px; font-weight: 400; }
  .contact-detail { display: flex; justify-content: flex-end; align-items: center; font-size: 19px; font-weight: 600; line-height: 1; margin-top: 8px; white-space: nowrap; }
  .contact-detail svg { margin-right: 8px; }
</style>
</head>
<body>
<main class="poster">
  <div class="hero-photo" role="img" aria-label="Photo of two physicians in white coats with stethoscopes reviewing a spreadsheet on a laptop"></div>

  <svg class="hero-panel" width="848" height="628" viewBox="0 0 848 628" aria-hidden="true">
    <defs>
      <linearGradient id="panelFill" x1="0" y1="0" x2="1" y2="1">
        <stop offset="0" stop-color="#2a9ddd"/>
        <stop offset="1" stop-color="#1b88cc"/>
      </linearGradient>
    </defs>
    <polygon points="0,285 428,285 553,628 0,628" fill="url(#panelFill)"/>
  </svg>

  <div class="brand">
    <div class="brand-mark"></div>
    <div class="brand-name">HARBOR CREST</div>
    <div class="brand-tagline">PHYSICIAN ADVISING</div>
  </div>

  <h1 class="headline">
    <span class="headline-text headline-accent">GET PAID</span>
    <span class="headline-text headline-care">FOR THE CARE</span>
    <span class="headline-text headline-provide">YOU PROVIDE</span>
  </h1>
  <div class="headline-rule"></div>
  <p class="subhead">Certified Physician Advisors<br>80+ Years Clinical Experience</p>

  <div class="money-photo" role="img" aria-label="Photo of a hand pulling banknotes from a glass jar of money on a round wooden board"></div>

  <h2 class="section-title title-stats">
    <svg width="30" height="32" viewBox="0 0 30 32"><rect x="0" y="22" width="7" height="10" fill="#12a98c"/><rect x="10" y="16" width="7" height="16" fill="#12a98c"/><rect x="20" y="10" width="7" height="22" fill="#12a98c"/><path d="M1 16 L12 8 L17 11 L28 2" stroke="#12a98c" stroke-width="2.2" fill="none"/><path d="M23 1 L29 1 L29 7" stroke="#12a98c" stroke-width="2.2" fill="none"/></svg>
    SUCCESS STATS
  </h2>
  <ul class="list stats-list">
    <li><svg width="15" height="15" viewBox="0 0 15 15"><rect x="1" y="1" width="12" height="12" fill="none" stroke="#12a98c" stroke-width="1.5"/><path d="M3.5 7 L6.5 10 L14 2" stroke="#12a98c" stroke-width="1.8" fill="none"/></svg>Over 60% Peer to Peer Appeals win rate (Medicare Advantage)</li>
    <li><svg width="15" height="15" viewBox="0 0 15 15"><rect x="1" y="1" width="12" height="12" fill="none" stroke="#12a98c" stroke-width="1.5"/><path d="M3.5 7 L6.5 10 L14 2" stroke="#12a98c" stroke-width="1.8" fill="none"/></svg>Over 50% success in first-level Letter Appeals</li>
  </ul>

  <h2 class="section-title title-services">
    <svg width="34" height="34" viewBox="0 0 34 34"><rect x="12" y="2" width="14" height="18" fill="none" stroke="#1e8fd6" stroke-width="2"/><path d="M15 8 H23 M15 12 H23 M15 16 H20" stroke="#1e8fd6" stroke-width="1.8"/><path d="M2 24 Q8 20 14 24 L22 24 Q24 27 20 28 L12 28 M2 30 Q12 33 22 30 L31 22" stroke="#1e8fd6" stroke-width="2" fill="none"/></svg>
    SERVICES OFFERED
  </h2>
  <ul class="list services-list">
    <li><svg width="15" height="15" viewBox="0 0 15 15"><rect x="1" y="1" width="12" height="12" fill="none" stroke="#2c95d6" stroke-width="1.5"/><path d="M3.5 7 L6.5 10 L14 2" stroke="#2c95d6" stroke-width="1.8" fill="none"/></svg>Payer Denial Management</li>
    <li><svg width="15" height="15" viewBox="0 0 15 15"><rect x="1" y="1" width="12" height="12" fill="none" stroke="#2c95d6" stroke-width="1.5"/><path d="M3.5 7 L6.5 10 L14 2" stroke="#2c95d6" stroke-width="1.8" fill="none"/></svg>Utilization Management</li>
    <li><svg width="15" height="15" viewBox="0 0 15 15"><rect x="1" y="1" width="12" height="12" fill="none" stroke="#2c95d6" stroke-width="1.5"/><path d="M3.5 7 L6.5 10 L14 2" stroke="#2c95d6" stroke-width="1.8" fill="none"/></svg>Clinical Documentation Integrity</li>
    <li><svg width="15" height="15" viewBox="0 0 15 15"><rect x="1" y="1" width="12" height="12" fill="none" stroke="#2c95d6" stroke-width="1.5"/><path d="M3.5 7 L6.5 10 L14 2" stroke="#2c95d6" stroke-width="1.8" fill="none"/></svg>Peer to Peer Appeals</li>
    <li><svg width="15" height="15" viewBox="0 0 15 15"><rect x="1" y="1" width="12" height="12" fill="none" stroke="#2c95d6" stroke-width="1.5"/><path d="M3.5 7 L6.5 10 L14 2" stroke="#2c95d6" stroke-width="1.8" fill="none"/></svg>Letter Appeal Management</li>
    <li><svg width="15" height="15" viewBox="0 0 15 15"><rect x="1" y="1" width="12" height="12" fill="none" stroke="#2c95d6" stroke-width="1.5"/><path d="M3.5 7 L6.5 10 L14 2" stroke="#2c95d6" stroke-width="1.8" fill="none"/></svg>Other Physician Advising Services</li>
  </ul>

  <h2 class="section-title title-strength">
    <svg width="32" height="32" viewBox="0 0 32 32"><rect x="12" y="1" width="14" height="30" fill="#ee7325"/><rect x="26" y="10" width="5" height="21" fill="#f08f49"/><path d="M15 5 h3 M21 5 h3 M15 10 h3 M21 10 h3 M15 15 h3 M21 15 h3 M15 20 h3 M21 20 h3" stroke="#fff" stroke-width="2.5"/><circle cx="9" cy="23" r="8" fill="#ee7325" stroke="#fff" stroke-width="1.5"/><path d="M5 23 L8 26 L13 20" stroke="#fff" stroke-width="2" fill="none"/></svg>
    COMPANY STRENGTH
  </h2>
  <ul class="list strength-list">
    <li><svg width="15" height="15" viewBox="0 0 15 15"><rect x="1" y="1" width="12" height="12" fill="none" stroke="#f08f49" stroke-width="1.5"/><path d="M3.5 7 L6.5 10 L14 2" stroke="#f08f49" stroke-width="1.8" fill="none"/></svg>Certified Physician Advisors</li>
    <li><svg width="15" height="15" viewBox="0 0 15 15"><rect x="1" y="1" width="12" height="12" fill="none" stroke="#f08f49" stroke-width="1.5"/><path d="M3.5 7 L6.5 10 L14 2" stroke="#f08f49" stroke-width="1.8" fill="none"/></svg>80+ Years Combined Clinical Experience</li>
    <li><svg width="15" height="15" viewBox="0 0 15 15"><rect x="1" y="1" width="12" height="12" fill="none" stroke="#f08f49" stroke-width="1.5"/><path d="M3.5 7 L6.5 10 L14 2" stroke="#f08f49" stroke-width="1.8" fill="none"/></svg>Small Company = Affordable Rate</li>
  </ul>

  <svg class="contact-panel" width="848" height="1200" viewBox="0 0 848 1200" aria-hidden="true">
    <polygon points="460,1040 848,1040 848,1200 384,1200" fill="#14ae8f"/>
  </svg>

  <section class="contact">
    <h2 class="contact-title">CONTACT US TODAY</h2>
    <div class="contact-rule"></div>
    <p class="contact-line">We Can Improve Your Revenue.</p>
    <p class="contact-detail">
      <svg width="18" height="18" viewBox="0 0 18 18"><rect width="18" height="18" rx="5" fill="#fff"/><path d="M5 4 L7.5 4 L8.5 7 L7 8 Q8 10.5 10 11 L11 9.5 L14 10.5 L14 13 Q9 14 6 10 Q4 7 5 4 Z" fill="#14ae8f"/></svg>
      304-555-0183
    </p>
    <p class="contact-detail">
      <svg width="18" height="18" viewBox="0 0 18 18"><rect width="18" height="18" rx="5" fill="#fff"/><rect x="4" y="5.5" width="10" height="7.5" rx="1" fill="none" stroke="#14ae8f" stroke-width="1.5"/><path d="M4.5 6.5 L9 10 L13.5 6.5" stroke="#14ae8f" stroke-width="1.5" fill="none"/></svg>
      info@harborcrestadvising.com
    </p>
  </section>
</main>
</body>
</html>
```